Editorial Website Design for High-End Custom Millwork Firm

Design (no development) for a 5-7 page website for a high-end custom architectural millwork firm. Editorial, magazine-quality aesthetic — think Dwelling Quarterly and top-tier millwork studios (Owen Tallard, Vorko). Full brief, reference sites, and project photography attached. We have uploaded a sample of our photography to use in your design. PLEASE READ PDF DOCUMENT BRIEF!!!

```html
<!DOCTYPE html>
<html lang="en">
<head>
<meta charset="utf-8">
<title>The Calloway Residence — Harlow Vane Millwork</title>
<link href="https://fonts.googleapis.com/css2?family=Newsreader:ital,opsz,wght@0,6..72,300;0,6..72,400;1,6..72,300;1,6..72,400&family=Inter:wght@400;500;600&display=swap" rel="stylesheet">
<style>
:root{
  --paper:#f8f7f2;
  --paper-2:#f0efe9;
  --ink:#1c1c1a;
  --ink-soft:#55544f;
  --muted:#8a8880;
  --rule:#dcdad3;
  --night:#000;
  --night-rule:#2a2a2a;
  --white:#fff;
}
*{margin:0;padding:0;box-sizing:border-box}
html,body{width:1200px;height:5128px;overflow:hidden}
body{background:var(--paper);color:var(--ink);font-family:"Inter",sans-serif;position:relative}
.serif{font-family:"Newsreader",serif;font-weight:300}
.label{font-size:10px;letter-spacing:.14em;text-transform:uppercase;font-weight:600}
.abs{position:absolute}

/* header */
.site-header{position:absolute;top:0;left:0;width:1200px;height:84px;background:rgba(240,239,234,.9);display:flex;align-items:center;justify-content:space-between;padding:0 74px 0 76px;z-index:3}
.brand{font-family:"Newsreader",serif;font-size:24px;font-weight:400;letter-spacing:-.01em;white-space:nowrap}
.nav{display:flex;gap:38px;font-size:11px;font-weight:500}
.nav a{color:var(--ink);text-decoration:none}
.nav .current{border-bottom:1px solid var(--ink);padding-bottom:4px}

/* hero */
.hero{position:absolute;top:0;left:0;width:1200px;height:934px;background:linear-gradient(180deg,#c9cbc4 0%,#a9afab 45%,#7c827f 100%)}
.hero-shade{position:absolute;inset:0;background:linear-gradient(180deg,rgba(0,0,0,0) 40%,rgba(0,0,0,.45) 100%)}
.hero-eyebrow{left:76px;top:586px;color:var(--white)}
.hero-title{left:76px;top:608px;font-size:78px;line-height:98px;color:var(--white)}
.hero-meta{left:76px;top:842px;color:rgba(255,255,255,.85);display:flex;gap:34px}
.hero-cue{left:1108px;top:872px}

/* intro */
.intro{position:absolute;top:934px;left:0;width:1200px;height:632px}
.intro h2{position:absolute;left:76px;top:142px;font-size:44px;line-height:52px;width:390px}
.intro .rule{position:absolute;left:76px;top:340px;width:90px;height:1px;background:var(--rule)}
.intro .copy{position:absolute;left:616px;top:148px;width:510px;color:var(--ink-soft)}
.intro .lead{font-size:15.5px;line-height:30px;margin-bottom:22px}
.intro .sub{font-size:13.5px;line-height:26px}

/* process */
.process{position:absolute;top:1566px;left:0;width:1200px;height:942px;background:var(--night);color:var(--white)}
.process .photo{position:absolute;left:76px;top:144px;width:510px;height:640px;background:linear-gradient(160deg,#6b6b6b,#2f2f2f 60%,#1a1a1a)}
.process .eyebrow{left:706px;top:146px;color:#9a9a9a;font-weight:500}
.process h2{position:absolute;left:706px;top:176px;font-family:"Newsreader",serif;font-size:46px;line-height:53px;font-weight:300}
.steps{position:absolute;left:706px;top:362px;width:420px}
.step{display:flex;gap:18px;padding:14px 0 24px;border-bottom:1px solid var(--night-rule);margin-bottom:26px;min-height:118px}
.step .num{font-size:10px;color:#8a8a8a;width:16px;padding-top:2px}
.step h3{font-size:10.5px;letter-spacing:.12em;font-weight:600;margin-bottom:12px}
.step p{font-size:14px;line-height:26px;color:#c6c6c6}

/* specifications */
.specs{position:absolute;top:2508px;left:0;width:1200px;height:572px}
.specs .head{left:76px;top:146px;color:var(--ink-soft)}
.specs .head-rule{left:76px;top:170px;width:108px;height:1px;background:var(--rule)}
.spec{position:absolute;width:320px}
.spec .label{font-size:9.5px;color:var(--muted);font-weight:500;display:block;margin-bottom:6px}
.spec p{font-size:16px}
.specs .detail{left:796px;top:242px;width:330px;height:186px;background:linear-gradient(90deg,#e9e8e4 0 30%,#c9a67a 30% 38%,#e4e3df 38%)}

/* gallery */
.gallery{position:absolute;top:3080px;left:0;width:1200px;height:836px}
.gallery .main{left:76px;top:6px;width:600px;height:752px;background:linear-gradient(170deg,#b6bfb9,#d8d8d2 55%,#e6e4de)}
.gallery .side{left:706px;top:6px;width:420px;height:348px;background:linear-gradient(160deg,#7e97a0,#a9b9bc 60%,#c7b08a)}
.gallery .rule{left:706px;top:384px;width:420px;height:1px;background:var(--rule)}
.quote{position:absolute;left:706px;top:632px;width:400px;font-family:"Newsreader",serif;font-style:italic;font-size:21px;line-height:34px;color:var(--ink-soft)}
.cite{left:706px;top:752px;font-size:10px}

/* next project */
.next{position:absolute;top:3916px;left:0;width:1200px;height:712px;background:linear-gradient(180deg,#2b4a79 0%,#40577a 30%,#6b5840 55%,#2e2a25 75%,#1d2530 100%);color:var(--white);text-align:center}
.next .eyebrow{position:absolute;top:280px;width:100%;color:rgba(255,255,255,.85);font-weight:500}
.next h2{position:absolute;top:300px;width:100%;font-size:44px}
.next svg{position:absolute;left:580px;top:390px}

/* footer */
.site-footer{position:absolute;top:4628px;left:0;width:1200px;height:500px;background:var(--paper-2)}
.site-footer .brand{position:absolute;left:76px;top:78px;font-size:23px}
.site-footer .about{position:absolute;left:76px;top:136px;width:300px;font-size:14px;line-height:26px}
.social{position:absolute;left:76px;top:250px;display:flex;gap:16px}
.social span{width:34px;height:34px;border:1px solid var(--rule);border-radius:50%;display:flex;align-items:center;justify-content:center}
.fcol{position:absolute;top:78px}
.fcol h4{font-size:10px;letter-spacing:.14em;font-weight:600;margin-bottom:22px}
.fcol li{list-style:none;font-size:14px;color:var(--ink-soft);margin-bottom:22px}
.fcol.contact li{color:var(--ink);margin-bottom:14px}
.footer-rule{position:absolute;left:76px;top:370px;width:1050px;height:1px;background:var(--rule)}
.legal{position:absolute;left:76px;top:408px;font-size:14px;color:var(--ink-soft)}
.legal-links{position:absolute;right:74px;top:408px;font-size:14px;color:var(--ink-soft);display:flex;gap:30px}
</style>
</head>
<body>

<section class="hero" role="img" aria-label="Photograph of a pale blue-grey painted bathroom vanity with patterned wallpaper, a pendant light and a freestanding tub">
  <div class="hero-shade"></div>
</section>

<header class="site-header">
  <div class="brand">HARLOW VANE MILLWORK</div>
  <nav class="nav">
    <a>Home</a><a class="current">Projects</a><a>Services</a><a>About</a><a>Blog</a><a>Contact</a>
  </nav>
</header>

<div class="abs label hero-eyebrow" style="font-weight:500">Case Study 04</div>
<h1 class="abs serif hero-title">The Calloway<br>Residence</h1>
<div class="abs label hero-meta" style="font-weight:500"><span>Oyster Bay, NY</span><span>GMA Premium Grade</span></div>
<svg class="abs hero-cue" width="16" height="16" viewBox="0 0 16 16"><path d="M3 5l5 5 5-5" fill="none" stroke="#fff" stroke-width="1.5"/></svg>

<section class="intro">
  <h2 class="serif">Crafting a legacy of precision and tactility.</h2>
  <div class="rule"></div>
  <div class="copy">
    <p class="lead">The Calloway Residence represents a pinnacle of contemporary residential millwork. Our brief was to create a seamless integration of functional storage and high-art aesthetic, utilizing European Oak and brushed metal accents to define the home's public and private volumes.</p>
    <p class="sub">The primary challenge involved the 14-foot vertical span of the main library wall, requiring invisible seismic anchoring and hand-matched grain patterns that flow uninterrupted across twenty-four individual cabinet faces. Every joinery detail was executed to GMA Premium Grade standards, ensuring not just visual perfection, but structural longevity for generations.</p>
  </div>
</section>

<section class="process">
  <div class="photo" role="img" aria-label="Black and white photograph of a craftsman planing a block of timber at a workbench"></div>
  <div class="abs label eyebrow">Our Process</div>
  <h2>From Raw Material<br>to<br>Refined Architecture.</h2>
  <div class="steps">
    <div class="step"><span class="num">01</span><div><h3>MATERIAL SOURCING</h3><p>Single-log veneer flitches are hand-selected to ensure tonal consistency across the entire residence.</p></div></div>
    <div class="step"><span class="num">02</span><div><h3>PRECISION MILLING</h3><p>CNC-guided precision meets hand-finished joinery for tolerances measured in fractions of a millimeter.</p></div></div>
    <div class="step"><span class="num">03</span><div><h3>GMA CERTIFICATION</h3><p>Third-party inspection confirms compliance with the most rigorous industry standards for premium grade millwork.</p></div></div>
  </div>
</section>

<section class="specs">
  <div class="abs label head">Specifications</div>
  <div class="abs head-rule"></div>
  <div class="spec" style="left:76px;top:242px"><span class="label">Species</span><p>Rift Sawn European White Oak</p></div>
  <div class="spec" style="left:436px;top:242px"><span class="label">Hardware</span><p>Halden Glide w/ Soft Close</p></div>
  <div class="spec" style="left:76px;top:346px"><span class="label">Finish</span><p>5% Sheen Polyurethane Matte</p></div>
  <div class="spec" style="left:436px;top:346px"><span class="label">Integration</span><p>Flush-mount LED Channels</p></div>
  <div class="abs detail" role="img" aria-label="Close-up photograph of an oak mortise joint"></div>
</section>

<section class="gallery">
  <div class="abs main" role="img" aria-label="Photograph of the bathroom vanity with arched mirror, wallpaper and upholstered stool"></div>
  <div class="abs side" role="img" aria-label="Photograph of a blue painted pantry with built-in ovens and glazed doors"></div>
  <div class="abs rule"></div>
  <blockquote class="quote">"Harlow Vane transformed our vision into a physical reality that feels solid, silent, and permanent. The wood choice speaks for itself."</blockquote>
  <div class="abs label cite">— Marcus Calloway, Client</div>
</section>

<section class="next" role="img" aria-label="Dusk photograph of a lit waterside pavilion reflected in water">
  <div class="label eyebrow">Next Project</div>
  <h2 class="serif">The Waterside Pavilion</h2>
  <svg width="40" height="24" viewBox="0 0 40 24"><path d="M2 12h34M26 3l10 9-10 9" fill="none" stroke="#fff" stroke-width="1.5"/></svg>
</section>

<footer class="site-footer">
  <div class="brand">HARLOW VANE MILLWORK</div>
  <p class="about">Dedicated to the highest standards of architectural woodwork for the most discerning clients across North America.</p>
  <div class="social">
    <span><svg width="12" height="12" viewBox="0 0 12 12"><circle cx="3" cy="6" r="1.3" fill="#555"/><circle cx="9" cy="3" r="1.3" fill="#555"/><circle cx="9" cy="9" r="1.3" fill="#555"/><path d="M3 6l6-3M3 6l6 3" stroke="#555" stroke-width=".8"/></svg></span>
    <span><svg width="12" height="12" viewBox="0 0 12 12"><circle cx="6" cy="6" r="4" fill="none" stroke="#555"/><circle cx="6" cy="6" r="1.6" fill="#555"/></svg></span>
  </div>
  <div class="fcol" style="left:436px"><h4>NAVIGATION</h4><ul><li>Portfolio</li><li>Our Shop</li><li>Capabilities</li><li>Careers</li></ul></div>
  <div class="fcol" style="left:616px"><h4>CERTIFICATION</h4><ul><li>GMA QCP Certified</li><li>MBE Certified</li><li>Sustainability</li></ul></div>
  <div class="fcol contact" style="left:796px"><h4>INQUIRIES</h4><ul><li>hello@harlowvane.com</li><li>+1 (555) 014-2290</li></ul></div>
  <div class="footer-rule"></div>
  <p class="legal">© 2024 Harlow Vane Millwork. Crafted to GMA Premium Grade Standards.</p>
  <div class="legal-links"><span>Privacy Policy</span><span>Terms of Service</span></div>
</footer>

</body>
</html>
```